Real Estate Biz Card

-Card Size: Standard
-Background: Dark grey or black. I am open to gradient or a textured background.
-Other Colors: I dont mind pops of color. Contrasty blue, lime green, red Etc. Feel free to get creative.
-Text color: be creative
-Font: I like modern styles. Something that works well with my KV718 logo. See attached
-I would like my logo (KV718) watermarked on the card. Either on one side or both.
-Front of Card: keep it simple. Head shot, name, Logo, Phone #
-Back: add the rest of the details. See list below.
-brokerages logo as well as the Domivest and Equal Housing Opportunity logos on the card
-Name: Tod Marwick
-Residential Real Estate
-Cell:
-Email:
-Site:
-Office Address:
-very small/fine print "Each office independently owned & operated

```html
<!DOCTYPE html>
<html lang="en">
<head>
<meta charset="utf-8">
<title>KV718 Business Card</title>
<link href="https://fonts.googleapis.com/css2?family=Montserrat:wght@400;500;600;700&display=swap" rel="stylesheet">
<style>
  :root {
    --stage: #d4d4d4;
    --card-dark-top: #2e3035;
    --card-dark-bottom: #141518;
    --brand-blue: #1e88e0;
    --text-light: #ffffff;
    --text-grey: #b4b8be;
    --watermark: rgba(255,255,255,0.06);
    --photo-top: #c9a98f;
    --photo-bottom: #4a6fa8;
  }
  * { box-sizing: border-box; margin: 0; padding: 0; }
  html, body {
    width: 1200px; height: 800px; overflow: hidden;
    background: var(--stage);
    font-family: "Montserrat", sans-serif;
  }
  .stage {
    width: 1200px; height: 800px;
    display: flex; align-items: center; justify-content: center; gap: 50px;
  }
  .card {
    width: 540px; height: 309px; position: relative; overflow: hidden;
    background: linear-gradient(160deg, var(--card-dark-top) 0%, var(--card-dark-bottom) 100%);
    box-shadow: 0 6px 18px rgba(0,0,0,0.25);
  }
  .watermark {
    position: absolute; color: var(--watermark);
    font-weight: 600; letter-spacing: 2px; line-height: 1;
    pointer-events: none;
  }
  /* Front */
  .front-watermark { right: 30px; bottom: 22px; font-size: 52px; }
  .front-brand {
    position: absolute; left: 40px; top: 48px;
    display: flex; align-items: center; gap: 10px;
    color: var(--brand-blue); font-weight: 600; font-size: 48px; letter-spacing: 1px; line-height: 1;
  }
  .brand-mark { width: 16px; height: 16px; background: currentColor; }
  .agent-name {
    position: absolute; left: 40px; top: 122px;
    color: var(--text-light); font-weight: 700; font-size: 19px; letter-spacing: 0.5px;
  }
  .agent-title {
    position: absolute; left: 40px; top: 147px;
    color: var(--brand-blue); font-weight: 500; font-size: 10.5px; letter-spacing: 1px;
  }
  .office-address {
    position: absolute; left: 40px; top: 174px;
    color: var(--text-grey); font-size: 12px; line-height: 17px;
  }
  .contact-list {
    position: absolute; left: 40px; top: 220px; list-style: none;
    color: var(--text-grey); font-size: 12px; line-height: 18px;
  }
  .contact-list li { display: flex; align-items: center; gap: 9px; }
  .contact-list svg { width: 10px; height: 10px; flex: none; }
  .headshot {
    position: absolute; right: 48px; top: 40px;
    width: 120px; height: 120px; border-radius: 50%;
    border: 2px solid var(--brand-blue);
    background: linear-gradient(180deg, var(--photo-top) 0%, var(--photo-top) 45%, var(--photo-bottom) 100%);
  }
  /* Back */
  .back-watermark { left: -20px; top: 6px; font-size: 150px; }
  .back-brand {
    position: absolute; left: 0; right: 0; top: 84px;
    display: flex; align-items: center; justify-content: center; gap: 14px;
    color: var(--text-light); font-weight: 600; font-size: 72px; letter-spacing: 2px; line-height: 1;
  }
  .back-brand .brand-mark { width: 22px; height: 22px; color: var(--brand-blue); }
  .affiliations {
    position: absolute; left: 0; right: 0; bottom: 62px;
    display: flex; align-items: center; justify-content: center; gap: 18px;
    color: var(--text-light);
  }
  .badge { width: 22px; height: 22px; background: var(--text-light); }
  .badge-house { border-radius: 3px; }
  .brokerage { font-weight: 600; font-size: 15px; letter-spacing: 0.5px; }
  .fine-print {
    position: absolute; left: 0; right: 0; bottom: 20px; text-align: center;
    color: var(--text-grey); font-size: 7.5px; letter-spacing: 0.5px;
  }
</style>
</head>
<body>
<main class="stage">
  <section class="card card-front">
    <span class="watermark front-watermark" aria-hidden="true">KV718</span>
    <div class="front-brand"><span>KV718</span><span class="brand-mark"></span></div>
    <h1 class="agent-name">TOD MARWICK</h1>
    <p class="agent-title">RESIDENTIAL REAL ESTATE</p>
    <p class="office-address">88 Alder Street<br>Larchmont, NJ, 07011</p>
    <ul class="contact-list">
      <li><svg viewBox="0 0 10 10"><path d="M2 1 L4 1 L4.5 3 L3.3 4 Q4.5 6 6 6.7 L7 5.5 L9 6 L9 8 Q5 9 2.5 6 Q1 4 2 1 Z" fill="#1e88e0"/></svg>+1.555.014.2276</li>
      <li><svg viewBox="0 0 10 10"><rect x="0.8" y="2" width="8.4" height="6" fill="none" stroke="#1e88e0" stroke-width="1.2"/><path d="M1 2.3 L5 5.5 L9 2.3" fill="none" stroke="#1e88e0" stroke-width="1.2"/></svg>hello@kv718homes.com</li>
      <li><svg viewBox="0 0 10 10"><circle cx="5" cy="5" r="4.2" fill="none" stroke="#1e88e0" stroke-width="1.2"/><path d="M1 5 H9 M5 1 Q2.5 5 5 9 M5 1 Q7.5 5 5 9" fill="none" stroke="#1e88e0" stroke-width="0.9"/></svg>www.kv718homes.com</li>
    </ul>
    <div class="headshot" role="img" aria-label="Headshot of the agent"></div>
  </section>

  <section class="card card-back">
    <span class="watermark back-watermark" aria-hidden="true">KV718</span>
    <div class="back-brand"><span>KV718</span><span class="brand-mark"></span></div>
    <div class="affiliations">
      <span class="badge badge-house" role="img" aria-label="Equal housing opportunity badge"></span>
      <span class="badge" role="img" aria-label="Domivest membership badge"></span>
      <span class="brokerage">Northgate Realty</span>
    </div>
    <p class="fine-print">Each office independently owned &amp; operated</p>
  </section>
</main>
</body>
</html>
```